Plakat für Hersteller von Maultaschen und Knödeln
Zielgruppe
Mit meiner Manufaktur Rinnfalten & Co stelle ich Maultaschen und Knödel her. Produziert wird mit hochwertigen, möglichst regionalen Zutaten und mit dem Anspruch, traditionelle Klassiker in zeitgemäßer Qualität anzubieten.
Im Mittelpunkt stehen Frische, Transparenz und ehrliches Handwerk. Die Produkte werden mit Sorgfalt hergestellt und sind für den direkten Verkauf auf dem Brunnwaldener Wochenmarkt bestimmt. Rinnfalten & Co verbindet bodenständige Küche mit regionaler Identität – unkompliziert, authentisch und genussorientiert.
Zielgruppe rund um den Brunnwaldener Wochenmarkt:
- Marktbesucher mit Qualitätsbewusstsein, die gezielt regionale und handwerklich hergestellte Lebensmittel kaufen
- Berufstätige und Familien, die hochwertige, frisch produzierte Gerichte für zu Hause suchen
- Genussorientierte Kundinnen und Kunden, die traditionelle Küche schätzen
- Seniorinnen und Senioren, die klassische Hausmannskost bevorzugen
- Regionalverbundenen Verbraucherinnen und Verbrauchern, die lokale Anbieter unterstützen möchten
Der Brunnwaldener Wochenmarkt zieht ein vielfältiges Publikum an, das Wert auf persönliche Beratung, Frische und nachvollziehbare Herkunft legt. Rinnfalten positioniert sich hier als authentischer, spezialisierter Anbieter für handgemachte Teigklassiker mit klarem kulinarischem Profil.
Aufgabenstellung
Das Plakat soll in A5, A4, A3 und A2 nutzbar sein und der Text soll austauschbar sein.
Das Plakat soll gut zum Wochenmarkt passen und ehrliches, qualitativ hochwertiges Handwerk ausdrücken und vor allem Lust auf Maultaschen und Knödel machen. Es soll zu meinen Marktstand (Monza Rot) und dem Logo passen. Das Logo soll sehr präsent sein.

```html
<!DOCTYPE html>
<html lang="de">
<head>
<meta charset="utf-8">
<title>Rinnfalten &amp; Co – Plakat</title>
<link rel="stylesheet" href="https://fonts.googleapis.com/css2?family=Oswald:wght@700&family=Lobster&family=Lato:wght@300;400;700&display=swap">
<style>
  :root {
    --monza-red: #a91f2b;
    --monza-red-dark: #8e1822;
    --cream: #f4e4a6;
    --badge-cream: #faf3bd;
    --paper-white: #ffffff;
    --ink: #1c1a1a;
    --ink-soft: #4a4646;
    --logo-red: #b0202c;
    --parchment-light: #e6d3a8;
    --parchment-dark: #a8874f;
  }
  * { margin: 0; padding: 0; box-sizing: border-box; }
  html, body { width: 800px; height: 1200px; overflow: hidden; background: #ffffff; }
  .poster {
    position: relative;
    width: 800px;
    height: 1200px;
    background: radial-gradient(ellipse at 30% 40%, var(--monza-red) 0%, var(--monza-red-dark) 100%);
    font-family: "Lato", sans-serif;
    overflow: hidden;
  }
  .logo-field { position: absolute; left: 0; top: 0; width: 380px; height: 225px; }
  .brand-name {
    position: absolute; left: 58px; top: 88px;
    display: flex; align-items: center; gap: 12px;
    font-family: "Lato", sans-serif; font-weight: 700; font-size: 28px;
    color: var(--logo-red); white-space: nowrap;
  }
  .brand-dot { width: 24px; height: 24px; border-radius: 50%; background: var(--logo-red); flex: none; }
  .headline {
    position: absolute; left: 46px; top: 245px;
    font-family: "Oswald", sans-serif; font-weight: 700;
    font-size: 68px; line-height: 66px; letter-spacing: 1px;
    color: var(--cream); text-transform: uppercase;
  }
  .subline {
    position: absolute; left: 50px; top: 458px;
    font-family: "Lobster", cursive; font-size: 24px; color: var(--cream);
  }
  .benefits { position: absolute; left: 46px; top: 538px; list-style: none; }
  .benefit { position: relative; padding-left: 30px; margin-bottom: 26px; }
  .benefit::before {
    content: ""; position: absolute; left: 0; top: 9px;
    width: 12px; height: 12px; border-radius: 50%;
    background: var(--cream); box-shadow: 0 0 0 3px rgba(244,228,166,0.35);
  }
  .benefit-title { font-family: "Lobster", cursive; font-size: 23px; color: var(--cream); line-height: 30px; }
  .benefit-text { font-weight: 300; font-size: 17px; color: #f7eaea; line-height: 28px; }
  .promise {
    position: absolute; left: 44px; top: 838px; width: 413px; height: 146px;
    background: var(--badge-cream); border-radius: 0 22px 0 0;
    display: flex; align-items: center;
  }
  .promise-seal { width: 82px; height: 110px; margin-left: 22px; margin-right: 38px; }
  .promise-list { list-style: none; font-weight: 700; font-size: 21px; color: var(--ink); line-height: 40px; }
  .scroll-visual {
    position: absolute; left: 500px; top: 42px; width: 300px; height: 940px;
    background: linear-gradient(90deg, var(--parchment-dark) 0%, var(--parchment-light) 30%, var(--parchment-light) 75%, var(--parchment-dark) 100%);
  }
  .food-photo { position: absolute; left: 570px; width: 222px; height: 210px; }
  .food-photo--dough { top: 189px; background: linear-gradient(160deg, #f1eee8 0%, #d9c3a4 100%); }
  .food-photo--knoedel { top: 409px; background: linear-gradient(160deg, #5e3f27 0%, #d8a55a 60%, #b9822f 100%); }
  .food-photo--maultasche { top: 628px; background: linear-gradient(160deg, #3d2c22 0%, #d6a449 55%, #6b4a2e 100%); }
  .market-band {
    position: absolute; left: 0; top: 1018px; width: 800px; height: 182px;
    background: var(--paper-white); text-align: center; padding-top: 40px;
  }
  .market-call { font-weight: 700; font-size: 26px; line-height: 40px; color: var(--ink); }
  .market-tagline { font-weight: 400; font-size: 17px; color: var(--ink-soft); margin-top: 12px; }
</style>
</head>
<body>
<main class="poster">
  <svg class="logo-field" viewBox="0 0 380 225" aria-hidden="true">
    <path d="M0 0 H375 C372 120 290 220 150 222 C80 223 30 205 0 190 Z" fill="#ffffff"/>
  </svg>
  <div class="brand-name"><span class="brand-dot"></span>Rinnfalten &amp; Co</div>

  <div class="scroll-visual" role="img" aria-label="Aufgerollte Pergamentrolle als Rahmen für die Produktfotos"></div>
  <div class="food-photo food-photo--dough" role="img" aria-label="Foto: Hände formen Maultaschen auf bemehlter Arbeitsfläche"></div>
  <div class="food-photo food-photo--knoedel" role="img" aria-label="Foto: aufgebrochener Knödel mit Soße und Schnittlauch"></div>
  <div class="food-photo food-photo--maultasche" role="img" aria-label="Foto: angebratene Maultasche mit Zwiebeln und Petersilie"></div>

  <h1 class="headline">Echt.<br>Handgemacht.<br>Lecker.</h1>
  <p class="subline">Maultaschen &amp; Knödel wie hausgemacht.</p>

  <ul class="benefits">
    <li class="benefit">
      <div class="benefit-title">Frische aus der Region:</div>
      <div class="benefit-text">Hochwertige Zutaten, ehrliches Handwerk.</div>
    </li>
    <li class="benefit">
      <div class="benefit-title">Tradition trifft Moderne:</div>
      <div class="benefit-text">Klassische Rezepte in zeitgemäßer Qualität.</div>
    </li>
    <li class="benefit">
      <div class="benefit-title">Direkt vom Erzeuger:</div>
      <div class="benefit-text">Mit Liebe in unserer Manufaktur hergestellt.</div>
    </li>
  </ul>

  <section class="promise">
    <svg class="promise-seal" viewBox="0 0 82 110" aria-hidden="true">
      <circle cx="41" cy="40" r="38" fill="var(--monza-red)"/>
    </svg>
    <ul class="promise-list">
      <li>100% Transparent</li>
      <li>100% Leidenschaft</li>
      <li>Regional verwurzelt</li>
    </ul>
  </section>

  <footer class="market-band">
    <p class="market-call">Besuchen Sie uns an unserem Stand (Monza-Rot)<br>auf dem Brunnwaldener Wochenmarkt!</p>
    <p class="market-tagline">Rinnfalten &amp; Co – Weil Qualität man schmeckt.</p>
  </footer>
</main>
</body>
</html>
```